Private Medical Clinic needs a letterhead design

Letterhead that can be edited. Letter head is needed for printing official doctor's notes, referrals, etc in a medical clinic. The letterhead should use the attached logos

```html
<!DOCTYPE html>
<html lang="en">
<head>
<meta charset="utf-8">
<title>Willow Bend Clinic Letterhead</title>
<link href="https://fonts.googleapis.com/css2?family=Lato:wght@400&family=Lora:wght@400&display=swap" rel="stylesheet">
<style>
  :root {
    --backdrop: #cbc0be;
    --paper: #fbfbf8;
    --band-green: #4a5449;
    --band-grey: #a9a9ab;
    --ink: #3d3f3c;
    --icon: #ffffff;
  }
  html, body {
    margin: 0;
    width: 1200px;
    height: 784px;
    overflow: hidden;
    background: var(--backdrop);
  }
  .letterhead {
    position: absolute;
    left: 348px;
    top: 30px;
    width: 512px;
    height: 724px;
    background: var(--paper);
    box-shadow: 0 2px 6px rgba(0,0,0,0.15);
  }
  .side-band-top {
    position: absolute;
    left: 0; top: 0;
    width: 20px; height: 150px;
    background: var(--band-grey);
  }
  .side-band-main {
    position: absolute;
    left: 0; top: 156px;
    width: 20px; bottom: 0;
    background: var(--band-green);
  }
  .brand {
    position: absolute;
    left: 52px;
    top: 40px;
    display: flex;
    align-items: center;
    gap: 10px;
    font-family: "Lora", serif;
    font-size: 30px;
    font-weight: 400;
    color: var(--ink);
  }
  .brand-dot {
    width: 16px; height: 16px;
    border-radius: 50%;
    background: var(--ink);
  }
  .contact-strip {
    position: absolute;
    left: 0;
    bottom: 38px;
    width: 30px;
    height: 122px;
    background: var(--band-green);
  }
  .contact-strip svg {
    position: absolute;
    left: 9px;
    width: 13px;
    height: 13px;
  }
  .contact-list {
    position: absolute;
    left: 40px;
    bottom: 40px;
    margin: 0;
    padding: 0;
    list-style: none;
    font-family: "Lato", sans-serif;
    font-size: 11px;
    line-height: 14px;
    color: var(--ink);
  }
  .contact-list .gap { height: 22px; }
</style>
</head>
<body>
  <main class="letterhead">
    <div class="side-band-top"></div>
    <div class="side-band-main"></div>

    <div class="brand"><span>Willow Bend</span><span class="brand-dot"></span></div>

    <div class="contact-strip">
      <svg style="top:8px" viewBox="0 0 12 12" aria-hidden="true">
        <path d="M6 1a3.5 3.5 0 0 0-3.5 3.5C2.5 7.5 6 11 6 11s3.5-3.5 3.5-6.5A3.5 3.5 0 0 0 6 1z" fill="var(--icon)"/>
        <circle cx="6" cy="4.5" r="1.3" fill="var(--band-green)"/>
      </svg>
      <svg style="top:56px" viewBox="0 0 12 12" aria-hidden="true">
        <path d="M3 1.5l2 2-1 1.2a6 6 0 0 0 3.3 3.3l1.2-1 2 2-1.3 1.5C5.5 10.3 1.7 6.5 1.5 2.8z" fill="var(--icon)"/>
      </svg>
      <svg style="top:78px" viewBox="0 0 12 12" aria-hidden="true">
        <rect x="1" y="2.5" width="10" height="7" fill="var(--icon)"/>
        <path d="M1 2.5l5 4 5-4" fill="none" stroke="var(--band-green)" stroke-width="1"/>
      </svg>
      <svg style="top:100px" viewBox="0 0 12 12" aria-hidden="true">
        <circle cx="6" cy="6" r="5" fill="var(--icon)"/>
        <path d="M1 6h10M6 1v10M6 1c-2.5 2.8-2.5 7.2 0 10M6 1c2.5 2.8 2.5 7.2 0 10" fill="none" stroke="var(--band-green)" stroke-width="0.7"/>
      </svg>
    </div>

    <ul class="contact-list">
      <li>1234 First Line Address</li>
      <li>5678 Second Line Address</li>
      <li class="gap"></li>
      <li>(111) 999-0000</li>
      <li>info@yourmail.com</li>
      <li>www.yourwebsite.com</li>
    </ul>
  </main>
</body>
</html>
```